Bramblewick Co Leaflet. A5 2-sided Flyer for a UK Lawn Treatment Company

I need an A5 two-side leaflet / flyer designed for my Lawn Treatment company. The leaflet will be for door-drops so quick impact needed. Full colour, both sides. I provide lawn treatments to customers in the Exeter area of Devon. I would like to design to be clear, fresh and reflect the joy a good lawn and garden can bring.

Target Market(s)

Home Owners. 30-80 Years. Familys

Font styles to use
Sans Serif

Colors
9bcb3c
f78f20
ec1f27
33a6d7

Requirements
Must have
• Good front page picture
• Logo
• Contact details on front.
• Call to Action
• More details in Text file included in design.
Nice to have
• Clipart of a family / lady enjoying a lawn.

```html
<!DOCTYPE html>
<html lang="en">
<head>
<meta charset="utf-8">
<title>Bramblewick Co Leaflet</title>
<link href="https://fonts.googleapis.com/css2?family=Roboto+Slab:wght@400;500;700;800&display=swap" rel="stylesheet">
<style>
:root{
  --leaf:#1e8a2a;
  --leaf-dark:#15641d;
  --lime:#9bcb3c;
  --sky:#a9cbee;
  --soil:#6b2f1a;
  --soil-text:#6e2414;
  --ink:#222;
  --mist:#ececec;
  --backdrop:#e6e6e3;
  --gold:#f0b020;
}
*{box-sizing:border-box;margin:0;padding:0}
html,body{width:1200px;height:1000px;overflow:hidden}
body{background:var(--backdrop);font-family:"Roboto Slab",serif;color:var(--ink);position:relative}
.page{position:absolute;top:160px;width:480px;height:680px;background:#fff;overflow:hidden;box-shadow:0 6px 18px rgba(0,0,0,.25)}
.front{left:90px}
.back{left:630px}
.abs{position:absolute}

/* front */
.front-photo{left:0;top:0;width:480px;height:580px;
  background:linear-gradient(180deg,#fbfcfb 0%,#e4ece4 16%,#93ad86 30%,#4f7d3a 45%,#6fa53b 58%,#5e9a2f 80%,#4f8a28 100%)}
.brand{right:40px;top:44px;display:flex;align-items:center;gap:12px}
.brand-dot{width:44px;height:44px;border-radius:50%;background:var(--leaf)}
.brand-name{font-weight:500;font-size:28px;color:var(--leaf);letter-spacing:.5px;white-space:nowrap}
.seal{left:315px;top:345px;width:120px;height:120px;border-radius:50%;background:var(--lime);border:6px solid #fff;box-shadow:0 2px 6px rgba(0,0,0,.3)}
.seal-core{position:absolute;left:22px;top:22px;width:64px;height:64px;border-radius:50%;background:#1d3242}
.front-waves{left:0;top:410px}
.headline{left:30px;top:540px;width:420px;text-align:center;white-space:nowrap}
.headline h1{font-size:26px;font-weight:800;color:var(--leaf-dark);line-height:1.05}
.headline h2{font-size:17px;font-weight:700;color:var(--leaf-dark);line-height:1.2}
.headline p{font-size:12.5px;font-weight:500;color:#1a1a1a;line-height:1.3}
.headline .num{color:var(--leaf)}
.web-band{left:0;top:636px;width:480px;height:28px;background:var(--leaf);color:#fff;text-align:center;font-size:14px;font-weight:700;line-height:28px}
.web-band span{color:var(--gold)}

/* back */
.back-photo{left:0;top:0;width:480px;height:240px;
  background:linear-gradient(180deg,#3f6a2e 0%,#6c9444 35%,#79b540 65%,#6aa838 100%)}
.back-waves{left:0;top:120px}
.circle-photo{border-radius:50%;border:6px solid var(--leaf)}
.circle-a{left:70px;top:60px;width:140px;height:140px;background:radial-gradient(circle at 50% 40%,#c9d8a0,#79b540 70%)}
.circle-b{left:180px;top:112px;width:120px;height:120px;background:radial-gradient(circle at 50% 45%,#9fc46a,#4f8a2a 75%)}
.col{left:18px;top:236px;width:236px;font-size:9.4px;line-height:1.22}
.col h3{font-size:10px;font-weight:700;color:var(--soil-text);margin-top:9px;text-transform:uppercase}
.col h3::before{content:"";display:inline-block;width:6px;height:6px;background:var(--leaf);margin-right:5px;vertical-align:1px}
.col .call{color:var(--leaf);font-weight:500}
.service-box{left:262px;top:256px;width:204px;height:222px;background:var(--mist);border-radius:10px;padding:10px 10px;font-size:9.2px;line-height:1.2}
.service-box h3{font-size:10px;font-weight:700;color:var(--soil-text);white-space:nowrap}
.service-list{list-style:none;margin-top:6px}
.service-list li{color:var(--leaf);font-weight:500;font-size:9px;line-height:13.5px;display:flex;align-items:center;gap:5px;white-space:nowrap}
.service-list svg{flex:none}
.save{left:262px;top:488px;width:204px;font-size:13px;font-weight:500;color:var(--leaf);line-height:1.05}
.testi-tab{left:18px;top:530px;width:138px;height:22px;background:var(--leaf);color:#fff;font-size:11px;font-weight:700;line-height:22px;padding-left:12px;border-radius:0 10px 0 0}
.testi-box{left:18px;top:552px;width:444px;height:58px;background:var(--soil);border-radius:0 12px 0 0;color:#fff;font-size:8.6px;font-style:italic;display:flex;gap:26px;padding:8px 14px;line-height:1.2}
.testi-box p{flex:1}
.bottom-waves{left:0;top:586px}
.cta{left:40px;top:632px;font-size:16px;font-weight:500;color:var(--soil-text);letter-spacing:.5px;white-space:nowrap}
.cta-web{left:84px;top:655px;font-size:11.5px;color:#333;white-space:nowrap}
.mark{left:372px;top:592px;width:84px;height:84px;border-radius:50%;border:3px solid var(--leaf);background:#fff;display:flex;align-items:center;justify-content:center;text-align:center}
.mark span{font-size:9.5px;font-weight:500;color:var(--leaf);line-height:1.15}
</style>
</head>
<body>

<section class="page front">
  <div class="abs front-photo" role="img" aria-label="Photo of a sunny garden with a neat green lawn and flowering borders"></div>
  <div class="abs brand"><div class="brand-dot"></div><div class="brand-name">BRAMBLEWICK CO</div></div>
  <div class="abs seal" aria-hidden="true"><div class="seal-core"></div></div>
  <svg class="abs front-waves" width="480" height="270" viewBox="0 0 480 270">
    <path d="M0 110 C120 60 300 60 480 0 L480 270 L0 270 Z" fill="var(--soil)"/>
    <path d="M0 130 C130 85 310 85 480 28 L480 270 L0 270 Z" fill="var(--sky)"/>
    <path d="M40 122 C120 84 210 78 280 92 C200 92 120 102 40 122 Z" fill="var(--leaf)"/>
  </svg>
  <div class="abs headline">
    <h1>TREATMENTS AND ADVICE</h1>
    <h2>TO KEEP YOUR LAWN LOOKING NICE</h2>
    <p>CALL TODAY ON <span class="num">01632 960418</span> OR <span class="num">TEXT 07700 900418</span></p>
    <p>BOOK YOUR LAWN SURVEY</p>
  </div>
  <div class="abs web-band">www.<span>bramblewickco</span>.co.uk</div>
</section>

<section class="page back">
  <div class="abs back-photo" role="img" aria-label="Photo of a striped lawn in a large garden with hedges and pots"></div>
  <svg class="abs back-waves" width="480" height="130" viewBox="0 0 480 130">
    <path d="M0 20 C60 70 160 110 300 100 C380 95 440 70 480 60 L480 130 L0 130 Z" fill="var(--leaf)"/>
    <path d="M0 38 C60 86 160 122 300 114 C380 110 440 92 480 84 L480 130 L0 130 Z" fill="#fff"/>
  </svg>
  <div class="abs circle-photo circle-a" role="img" aria-label="Photo of a family relaxing together on a lawn"></div>
  <div class="abs circle-photo circle-b" role="img" aria-label="Photo of a freshly striped garden lawn"></div>

  <div class="abs col">
    <h3>For a beautiful weed-free lawn</h3>
    <p>Call Bramblewick Co today and start your journey to a wonderful, lush, green lawn you and your family can enjoy. Arrange a no-obligation lawn survey and quotation at a time to suit you.</p>
    <p class="call">Call 01632 960418 now.</p>
    <h3>I will understand your lawn</h3>
    <p>Every lawn is unique. I take time to gain a comprehensive understanding of your lawn and its situation. I will also listen to you and understand your problems and your aspirations for your grass.</p>
    <h3>Your lawn treatments</h3>
    <p>I will create a custom treatment programme tailored to your lawn. I may also recommend some remedial treatments to correct any existing problems. There is no contract to sign. I guarantee all treatments.</p>
  </div>

  <div class="abs service-box">
    <h3>INDUSTRY-LEADING LAWN CARE</h3>
    <p>I have 8 years of experience in the leading edge of domestic lawn care. I have a comprehensive range of treatments including:</p>
    <ul class="service-list">
      <li><svg width="9" height="9" viewBox="0 0 10 10"><circle cx="5" cy="5" r="4.3" fill="none" stroke="currentColor"/><path d="M2.8 5.2l1.6 1.5 3-3.2" fill="none" stroke="currentColor" stroke-width="1.2"/></svg>SCARIFICATION</li>
      <li><svg width="9" height="9" viewBox="0 0 10 10"><circle cx="5" cy="5" r="4.3" fill="none" stroke="currentColor"/><path d="M2.8 5.2l1.6 1.5 3-3.2" fill="none" stroke="currentColor" stroke-width="1.2"/></svg>AERATION</li>
      <li><svg width="9" height="9" viewBox="0 0 10 10"><circle cx="5" cy="5" r="4.3" fill="none" stroke="currentColor"/><path d="M2.8 5.2l1.6 1.5 3-3.2" fill="none" stroke="currentColor" stroke-width="1.2"/></svg>MOSS CONTROL</li>
      <li><svg width="9" height="9" viewBox="0 0 10 10"><circle cx="5" cy="5" r="4.3" fill="none" stroke="currentColor"/><path d="M2.8 5.2l1.6 1.5 3-3.2" fill="none" stroke="currentColor" stroke-width="1.2"/></svg>OVERSEEDING</li>
      <li><svg width="9" height="9" viewBox="0 0 10 10"><circle cx="5" cy="5" r="4.3" fill="none" stroke="currentColor"/><path d="M2.8 5.2l1.6 1.5 3-3.2" fill="none" stroke="currentColor" stroke-width="1.2"/></svg>TOP DRESSING</li>
      <li><svg width="9" height="9" viewBox="0 0 10 10"><circle cx="5" cy="5" r="4.3" fill="none" stroke="currentColor"/><path d="M2.8 5.2l1.6 1.5 3-3.2" fill="none" stroke="currentColor" stroke-width="1.2"/></svg>LAWN REPAIRS</li>
      <li><svg width="9" height="9" viewBox="0 0 10 10"><circle cx="5" cy="5" r="4.3" fill="none" stroke="currentColor"/><path d="M2.8 5.2l1.6 1.5 3-3.2" fill="none" stroke="currentColor" stroke-width="1.2"/></svg>FERTILISATION &amp; WEED CONTROL</li>
      <li><svg width="9" height="9" viewBox="0 0 10 10"><circle cx="5" cy="5" r="4.3" fill="none" stroke="currentColor"/><path d="M2.8 5.2l1.6 1.5 3-3.2" fill="none" stroke="currentColor" stroke-width="1.2"/></svg>PEST AND DISEASE MANAGEMENT</li>
      <li><svg width="9" height="9" viewBox="0 0 10 10"><circle cx="5" cy="5" r="4.3" fill="none" stroke="currentColor"/><path d="M2.8 5.2l1.6 1.5 3-3.2" fill="none" stroke="currentColor" stroke-width="1.2"/></svg>SPECIAL EVENT PREPARATION</li>
    </ul>
  </div>

  <div class="abs save">SAVE TIME AND MONEY AND LEAVE YOUR LAWN TO AN EXPERT.</div>

  <div class="abs testi-tab">TESTIMONIALS</div>
  <div class="abs testi-box">
    <p>"Thank you for keeping our lawn in great shape for so long, I've been really pleased with how it has looked since you took care of it." - Tom</p>
    <p>"My lawn has never looked better since the day that you started to look after it for me." - Mrs. Dale</p>
  </div>

  <svg class="abs bottom-waves" width="480" height="100" viewBox="0 0 480 100">
    <path d="M0 24 C120 4 260 24 360 44 C420 54 460 49 480 39 L480 100 L0 100 Z" fill="var(--leaf)"/>
    <path d="M0 34 C120 18 260 38 360 58 C420 68 460 64 480 56 L480 100 L0 100 Z" fill="#fff"/>
  </svg>
  <div class="abs cta">CALL 01632 960418 TODAY.</div>
  <div class="abs cta-web">www.bramblewickco.co.uk</div>
  <div class="abs mark"><span>BRAMBLEWICK<br>CO</span></div>
</section>

</body>
</html>
```